Will you marry me post card

I am just looking for a postcard to send my partner that will ask him to marry me.
I plan on creating about 200 of them and mailing them all at once so that he gets them all on the same day.
They should all be similar or could have a few different options.
I would like it simple, elegant, clean and crisp. No images, just text or icons

My only requirement is the text, "will you marry me?" in all lowercase -- any fonts, can be big, small, varying sizes, repeated, whole card, tiny space, don't care...just amazing design. BUT SIMPLE!

```html
<!DOCTYPE html>
<html lang="en">
<head>
<meta charset="utf-8">
<title>will you marry me? — postcard</title>
<link rel="stylesheet" href="https://fonts.googleapis.com/css2?family=Playfair+Display:ital,wght@1,700&display=swap">
<style>
  :root {
    --page: #ececec;
    --card-light: #ffffff;
    --card-dark: #111111;
    --ink: #161616;
    --gold-deep: #b8902e;
    --gold-mid: #e2c15a;
    --gold-light: #f1db86;
  }
  * { margin: 0; padding: 0; box-sizing: border-box; }
  html, body {
    width: 1200px;
    height: 1000px;
    overflow: hidden;
    background: var(--page);
  }
  .postcard {
    position: absolute;
    left: 337px;
    width: 524px;
    height: 405px;
    overflow: hidden;
  }
  .postcard--light { top: 76px; background: var(--card-light); color: var(--ink); }
  .postcard--dark { top: 515px; background: var(--card-dark); }

  .proposal {
    font-family: "Playfair Display", "Didot", serif;
    font-style: italic;
    font-weight: 700;
    font-size: 58px;
    line-height: 1;
    letter-spacing: 0;
  }
  .proposal__word { position: absolute; white-space: nowrap; }
  .proposal__word--will  { left: 156px; top: 70px; }
  .proposal__word--you   { left: 264px; top: 86px; }
  .proposal__word--marry { left: 173px; top: 153px; }
  .proposal__word--me    { left: 200px; top: 229px; }

  .postcard--dark .proposal__word {
    background: linear-gradient(100deg, var(--gold-deep) 0%, var(--gold-mid) 40%, var(--gold-light) 60%, var(--gold-deep) 100%);
    -webkit-background-clip: text;
    background-clip: text;
    color: transparent;
  }

  .bow-tie {
    position: absolute;
    left: 218px;
    top: 302px;
    width: 66px;
    height: 38px;
  }
  .postcard--light .bow-tie { fill: var(--ink); }
</style>
</head>
<body>
  <section class="postcard postcard--light">
    <p class="proposal">
      <span class="proposal__word proposal__word--will">will</span>
      <span class="proposal__word proposal__word--you">you</span>
      <span class="proposal__word proposal__word--marry">marry</span>
      <span class="proposal__word proposal__word--me">me?</span>
    </p>
    <svg class="bow-tie" viewBox="0 0 66 38" aria-hidden="true">
      <polygon points="0,0 33,19 0,38"/>
      <polygon points="66,0 33,19 66,38"/>
    </svg>
  </section>

  <section class="postcard postcard--dark">
    <p class="proposal">
      <span class="proposal__word proposal__word--will">will</span>
      <span class="proposal__word proposal__word--you">you</span>
      <span class="proposal__word proposal__word--marry">marry</span>
      <span class="proposal__word proposal__word--me">me?</span>
    </p>
    <svg class="bow-tie" viewBox="0 0 66 38" aria-hidden="true">
      <defs>
        <linearGradient id="gold-foil" x1="0" y1="0" x2="1" y2="1">
          <stop offset="0" stop-color="#b8902e"/>
          <stop offset="0.5" stop-color="#f1db86"/>
          <stop offset="1" stop-color="#b8902e"/>
        </linearGradient>
      </defs>
      <polygon points="0,0 33,19 0,38" fill="url(#gold-foil)"/>
      <polygon points="66,0 33,19 66,38" fill="url(#gold-foil)"/>
    </svg>
  </section>
</body>
</html>
```